Business cards for Brightmarrow Consulting with the following info for the front side:

Brightmarrow Consulting
Executive Coaching and Human Capital Strategy
www.brightmarrow.example

Lorena Vaduvic
Principal
lorena@brightmarrow.example
+1 604 555 0172

Black background, text using the colours of the logo - enclosed.

The back side of the business card should feature the logo in the middle, with "Executive Coaching and Human Capital Strategy" on top and "www.brightmarrow.example" below.

```html
<!DOCTYPE html>
<html lang="en">
<head>
<meta charset="utf-8">
<title>Brightmarrow Consulting – Business Cards</title>
<link href="https://fonts.googleapis.com/css2?family=Lato:wght@400;700;900&display=swap" rel="stylesheet">
<style>
  :root {
    --brand-blue: #33a3da;
    --brand-yellow: #f6b917;
    --ink: #3a3a3a;
    --paper: #ffffff;
    --stage: #2b2b2d;
  }
  * { margin: 0; padding: 0; box-sizing: border-box; }
  html, body { width: 1200px; height: 900px; overflow: hidden; }
  body {
    background: var(--stage);
    font-family: "Lato", sans-serif;
    position: relative;
  }
  .card {
    position: absolute;
    left: 250px;
    width: 700px;
    height: 400px;
    border-radius: 18px;
    overflow: hidden;
  }
  /* back side */
  .card--back { top: 30px; background: var(--brand-blue); color: var(--paper); }
  .back-brand {
    position: absolute; left: 0; right: 0; top: 120px;
    display: flex; align-items: center; justify-content: center; gap: 18px;
  }
  .brand-mark {
    width: 78px; height: 78px; border-radius: 50%;
    border: 4px solid var(--paper);
    flex: none;
  }
  .back-brand-text { display: flex; flex-direction: column; }
  .brand-name {
    font-weight: 700; font-size: 50px; letter-spacing: 1px; line-height: 1;
  }
  .back-tagline { font-size: 17px; margin-top: 8px; letter-spacing: 0.3px; }
  .back-domain {
    font-size: 14px; letter-spacing: 4px; margin-top: 8px; text-align: right;
  }
  .back-domain .accent, .back-web .accent { color: var(--brand-yellow); }
  .back-web {
    position: absolute; left: 0; right: 0; bottom: 56px;
    text-align: center; font-size: 15px; letter-spacing: 4px;
  }
  /* front side */
  .card--front { top: 470px; background: var(--paper); }
  .front-swoosh { position: absolute; inset: 0; }
  .front-brand {
    position: absolute; left: 48px; top: 176px;
    display: flex; align-items: center; gap: 8px;
    color: var(--brand-blue);
  }
  .front-brand .brand-mark { width: 40px; height: 40px; border: 3px solid var(--brand-blue); }
  .front-brand .brand-name { font-size: 24px; letter-spacing: 0.5px; }
  .divider {
    position: absolute; left: 362px; top: 70px; width: 1px; height: 190px;
    background: var(--brand-yellow);
  }
  .contact {
    position: absolute; left: 392px; top: 36px; color: var(--ink);
  }
  .person-name { color: var(--brand-blue); font-weight: 900; font-size: 30px; line-height: 1.1; }
  .person-role { font-size: 17px; margin-bottom: 10px; }
  .company { color: var(--brand-yellow); font-weight: 700; font-size: 17px; line-height: 1.25; }
  .tagline { font-size: 16px; line-height: 1.3; margin-bottom: 10px; }
  .contact-list { list-style: none; }
  .contact-list li {
    display: flex; align-items: center; gap: 10px;
    font-size: 15px; line-height: 1.55;
  }
  .contact-list svg { width: 15px; height: 15px; flex: none; }
</style>
</head>
<body>

<section class="card card--back" aria-label="Business card back">
  <div class="back-brand">
    <span class="brand-mark" aria-hidden="true"></span>
    <div class="back-brand-text">
      <span class="brand-name">BRIGHTMARROW</span>
      <span class="back-tagline">Executive Coaching and Human Capital Strategy</span>
      <span class="back-domain"><span class="accent">brightmarrow</span>.example</span>
    </div>
  </div>
  <p class="back-web">www.<span class="accent">brightmarrow</span>.example</p>
</section>

<section class="card card--front" aria-label="Business card front">
  <svg class="front-swoosh" viewBox="0 0 700 400" preserveAspectRatio="none" aria-hidden="true">
    <path d="M60,400 Q480,370 700,305 L700,400 Z" fill="var(--brand-blue)"/>
    <path d="M320,392 Q575,352 700,300" fill="none" stroke="var(--brand-yellow)" stroke-width="5"/>
    <path d="M300,385 Q560,345 700,285" fill="none" stroke="var(--brand-blue)" stroke-width="4"/>
  </svg>

  <div class="front-brand">
    <span class="brand-mark" aria-hidden="true"></span>
    <span class="brand-name">BRIGHTMARROW</span>
  </div>

  <div class="divider" aria-hidden="true"></div>

  <div class="contact">
    <h1 class="person-name">Lorena Vaduvic</h1>
    <p class="person-role">Principal</p>
    <p class="company">Brightmarrow Consulting</p>
    <p class="tagline">Executive Coaching and Human<br>Capital Strategy</p>
    <ul class="contact-list">
      <li>
        <svg viewBox="0 0 16 16" aria-hidden="true"><path d="M3 1.5l2.5 0 1 3.5-1.6 1.2a8 8 0 0 0 4.9 4.9L11 9.5l3.5 1v2.5c0 .8-.7 1.5-1.5 1.5C7 14.5 1.5 9 1.5 3c0-.8.7-1.5 1.5-1.5z" fill="var(--brand-yellow)"/></svg>
        +1 604 555 0172
      </li>
      <li>
        <svg viewBox="0 0 16 16" aria-hidden="true"><rect x="1" y="3" width="14" height="10" rx="1" fill="var(--brand-yellow)"/><path d="M1.5 3.5L8 9l6.5-5.5" fill="none" stroke="#fff" stroke-width="1.2"/></svg>
        lorena@brightmarrow.example
      </li>
      <li>
        <svg viewBox="0 0 16 16" aria-hidden="true"><circle cx="8" cy="8" r="6.5" fill="var(--brand-yellow)"/><path d="M1.5 8h13M8 1.5c-3 3.5-3 9.5 0 13M8 1.5c3 3.5 3 9.5 0 13" fill="none" stroke="#fff" stroke-width="0.9"/></svg>
        www.brightmarrow.example
      </li>
    </ul>
  </div>
</section>

</body>
</html>
```